Presentation folder for holding wedding cake literature

We need to have a front cover design as well as a back cover design for a presentation folder to hold literature for a bakery who sells a lot of wedding cakes.

We have uploaded a couple copies of ideas that we like. They are for demonstrative purposes only.

The text on the front cover needs to be:
-The Frosting Parlour-
-Designing, baking and decorating perfect wedding cakes...Guaranteed!

On the back cover it needs to say:
-Serving VELVETcrumb cakes and a "Silver Ribbon" Experience-

In addition the back cover must contain the "Silver Ribbon Baker" logo.

We will only supply photos if necessary. We would rather have you choose them.

We are open to any colors as long as they are soft.

For a reference of the client, go to http://www.brindlefrostingparlour.example

Target Market(s)

The target market is primarily women ages 25-40.

Industry/Entity Type

Wedding

Requirements
Must have
• Must have priorities are listed in the brief.
Nice to have
• Fonts should be a combination of "script" and one or more complementary styles.

Colors should be either a soft blue, pinkish tone or lavender tone. Mixing any of the colors with a light gray would be acceptable as well.
Should not have
• No dark colors such as black, red, purple, green or orange.

```html
<!DOCTYPE html>
<html lang="en">
<head>
<meta charset="utf-8">
<title>The Frosting Parlour – Presentation Folder</title>
<link rel="stylesheet" href="https://fonts.googleapis.com/css2?family=Yanone+Kaffeesatz:wght@400;600&family=Arimo&display=swap">
<style>
  :root {
    --pink-top: #f6a9d4;
    --pink-mid: #f9c3e1;
    --pink-soft: #fce0ef;
    --white: #ffffff;
    --magenta: #e23fb7;
    --tile-rose: #f08fc6;
    --tile-blush: #f7c6df;
    --tile-lilac: #e2d3e6;
    --tile-cream: #f8f1b8;
    --photo-grey: #9ea4ab;
    --photo-mauve: #b59aa8;
    --photo-ivory: #eee7dc;
  }
  * { margin: 0; padding: 0; box-sizing: border-box; }
  html, body { width: 1200px; height: 848px; overflow: hidden; background: var(--pink-mid); }
  .folder {
    position: relative; width: 1200px; height: 848px; overflow: hidden;
    background: linear-gradient(180deg, var(--pink-top) 0%, var(--pink-mid) 45%, var(--pink-soft) 70%, var(--pink-mid) 100%);
    font-family: "Yanone Kaffeesatz", "Arial Narrow", sans-serif;
  }
  .waves { position: absolute; inset: 0; }
  .back-tagline {
    position: absolute; left: 78px; top: 150px; width: 470px;
    color: var(--white); font-size: 30px; line-height: 43px; letter-spacing: 0.3px;
  }
  .back-tagline span { display: block; }
  .back-tagline .line-two { text-align: right; }
  .back-tagline strong { font-weight: 600; }
  .front-title {
    position: absolute; left: 700px; top: 78px; width: 410px; text-align: center;
    font-family: "Yanone Kaffeesatz", "Arial Narrow", sans-serif;
    font-weight: 400; color: var(--magenta);
    font-size: 84px; line-height: 84px; white-space: nowrap;
  }
  .front-title span { display: block; }
  .front-promise {
    position: absolute; left: 860px; top: 718px; width: 320px; text-align: center;
    color: var(--white); font-size: 25px; line-height: 31px;
  }
  .front-promise .accent { color: var(--magenta); }
  .front-promise .guarantee { font-size: 30px; line-height: 36px; }
  .maker {
    position: absolute; left: 212px; top: 650px;
  }
  .maker-name {
    display: flex; align-items: center; gap: 10px; white-space: nowrap;
    font-size: 36px; color: var(--magenta); font-weight: 400; line-height: 40px;
  }
  .maker-name .dot { width: 16px; height: 16px; border-radius: 50%; background: var(--magenta); flex: none; }
  .contact {
    position: absolute; left: 199px; top: 732px;
    font-family: "Arimo", Arial, sans-serif; color: var(--magenta); font-size: 13px; line-height: 24px;
  }
  .contact .phone { display: flex; align-items: center; gap: 6px; padding-left: 47px; font-size: 16px; }
</style>
</head>
<body>
<main class="folder">
  <svg class="waves" width="1200" height="848" viewBox="0 0 1200 848">
    <defs>
      <linearGradient id="inner-glow" x1="0" y1="0" x2="0" y2="1">
        <stop offset="0" stop-color="#ffffff" stop-opacity="0.75"/>
        <stop offset="1" stop-color="#fbd3e8" stop-opacity="0.2"/>
      </linearGradient>
      <clipPath id="gallery-clip">
        <path d="M600,262 C700,240 800,330 900,345 C1000,355 1100,305 1200,285 L1200,570 C1050,620 900,690 700,690 L600,690 Z"/>
      </clipPath>
    </defs>
    <path class="inner-band" d="M0,280 C200,300 450,290 600,262 C700,240 800,330 900,345 C1000,355 1100,305 1200,285 L1200,570 C1050,620 900,690 700,690 C500,690 300,420 0,350 Z" fill="url(#inner-glow)"/>
    <g class="gallery" clip-path="url(#gallery-clip)" role="img" aria-label="Grid of wedding cake photographs with tiered white, lavender and mint cakes, bouquets and wedding rings">
      <rect x="600" y="282" width="66" height="72" fill="var(--tile-blush)"/>
      <rect x="686" y="282" width="80" height="72" fill="var(--tile-rose)"/>
      <rect x="776" y="282" width="77" height="72" fill="var(--tile-lilac)"/>
      <rect x="1043" y="282" width="68" height="72" fill="var(--tile-rose)"/>
      <rect x="1130" y="282" width="70" height="72" fill="var(--tile-cream)"/>
      <rect x="600" y="365" width="166" height="161" fill="var(--photo-mauve)"/>
      <rect x="776" y="365" width="77" height="78" fill="var(--photo-grey)"/>
      <rect x="864" y="365" width="78" height="78" fill="var(--photo-grey)"/>
      <rect x="952" y="365" width="80" height="78" fill="var(--photo-ivory)"/>
      <rect x="1043" y="365" width="157" height="161" fill="var(--photo-grey)"/>
      <rect x="776" y="452" width="77" height="74" fill="var(--photo-grey)"/>
      <rect x="864" y="452" width="168" height="160" fill="var(--photo-mauve)"/>
      <rect x="600" y="535" width="78" height="77" fill="var(--photo-grey)"/>
      <rect x="688" y="535" width="78" height="77" fill="#a8c9c2"/>
      <rect x="776" y="535" width="77" height="77" fill="var(--photo-ivory)"/>
      <rect x="1043" y="535" width="78" height="77" fill="var(--photo-ivory)"/>
      <rect x="1130" y="535" width="70" height="77" fill="var(--tile-blush)"/>
      <rect x="600" y="621" width="78" height="60" fill="var(--tile-rose)"/>
      <rect x="688" y="621" width="78" height="60" fill="var(--tile-blush)"/>
      <rect x="776" y="621" width="77" height="60" fill="#f4e27a"/>
      <rect x="864" y="621" width="78" height="60" fill="#b6a9d8"/>
      <rect x="952" y="621" width="80" height="60" fill="var(--tile-rose)"/>
      <rect x="1043" y="621" width="78" height="60" fill="var(--tile-lilac)"/>
    </g>
    <path class="wave-top" d="M0,280 C200,300 450,290 600,262 C700,240 800,330 900,345 C1000,355 1100,305 1200,285" fill="none" stroke="var(--white)" stroke-width="20"/>
    <path class="wave-bottom" d="M0,350 C300,420 500,690 700,690 C900,690 1050,620 1200,570" fill="none" stroke="var(--white)" stroke-width="18"/>
  </svg>

  <p class="back-tagline">
    <span class="line-one">Serving VELVETcrumb cakes</span>
    <span class="line-two">and a <strong>"Silver Ribbon"</strong> Experience</span>
  </p>

  <h1 class="front-title">
    <span>The Frosting</span>
    <span>Parlour</span>
  </h1>

  <div class="maker">
    <p class="maker-name"><span class="dot"></span>Silver Ribbon Baker</p>
  </div>

  <div class="contact">
    <p class="site">www.brindlefrostingparlour.example</p>
    <p class="phone">
      <svg width="15" height="15" viewBox="0 0 16 16" aria-hidden="true">
        <circle cx="8" cy="8" r="7" fill="none" stroke="var(--magenta)" stroke-width="1.4"/>
        <path d="M5.3 4.4 L6.6 4.2 L7.3 6 L6.5 6.7 C6.9 7.7 7.6 8.5 8.6 9 L9.3 8.2 L11 8.9 L10.9 10.3 C8 10.6 5 7.5 5.3 4.4 Z" fill="var(--magenta)"/>
      </svg>
      555-014-7720
    </p>
  </div>

  <p class="front-promise">
    Designing, baking and decorating<br>
    <span class="accent">perfect wedding cakes...</span><br>
    <span class="guarantee">Guaranteed!</span>
  </p>
</main>
</body>
</html>
```